Website for our 3rd party logistics warehouse company

Our company is a 3rd party logistics company. We receive and ship other businesses products for them. We offer our services to other smaller businesses that do not have a warehouse to operate out of. We also help many Brindlemart businesses prepare their products to be sold on Brindlemart.

We are looking for a modern looking design for our website. Please see our attached logo for design ideas. We are open to changing logo colors for website.

We really like the look of the website www.quorvela.com

Target Market(s)

Other businesses and brands of products

Industry/Entity Type

Warehousing and shipping

Number of Pages Required

2 page

Requirements
Must have
• We need 2 pages. Our main landing page and a duplicate page with different information geared towards brands.
Nice to have
• I like the look of overlay/transparent sections. Please see quorvela.com there is a ribbon that shows "Partners".

```html
<!DOCTYPE html>
<html lang="en">
<head>
<meta charset="utf-8">
<title>Keelhaven 3PL</title>
<link href="https://fonts.googleapis.com/css2?family=Lato:wght@400;700;900&display=swap" rel="stylesheet">
<style>
:root{
  --yellow:#fbbc2e;
  --yellow-deep:#f5ad14;
  --navy:#1f2340;
  --ink:#1f1f1f;
  --text:#333333;
  --grey:#eeeeee;
  --dark:#1e1e1e;
  --darker:#161616;
  --white:#ffffff;
  --line:#bdbdbd;
}
*{box-sizing:border-box;margin:0;padding:0}
html,body{width:1200px;height:3638px;overflow:hidden}
body{font-family:'Lato',sans-serif;color:var(--text);background:var(--white);position:relative}
.abs{position:absolute}
.btn{position:absolute;display:flex;align-items:center;justify-content:center;background:var(--yellow);color:var(--ink);font-weight:900;font-size:17px;border-radius:30px;letter-spacing:.2px}
h2.section-title{position:absolute;font-weight:900;color:var(--ink);font-size:34px;letter-spacing:.3px}

/* hero */
.hero{position:absolute;left:0;top:0;width:1200px;height:738px;
  background:linear-gradient(100deg,#2d3440 0%,#4a3a2c 30%,#8a5a2a 55%,#b77a35 75%,#6b4a2a 100%);}
.hero-shade{position:absolute;inset:0;background:linear-gradient(90deg,rgba(0,0,0,.45) 0%,rgba(0,0,0,.15) 55%,rgba(0,0,0,0) 100%)}
.brand{position:absolute;left:75px;top:66px;display:flex;align-items:center;gap:10px;color:var(--white);font-weight:700;font-size:24px;letter-spacing:2px}
.brand-dot{width:14px;height:14px;border-radius:50%;background:var(--yellow)}
.hero-phone{position:absolute;left:812px;top:68px;display:flex;align-items:center;gap:8px;color:var(--yellow);font-size:25px;font-weight:700}
.menu-icon{position:absolute;left:1090px;top:70px;width:36px}
.menu-icon span{display:block;height:4px;background:var(--white);margin-bottom:8px;border-radius:1px}
.hero h1{position:absolute;left:75px;top:294px;color:var(--white);font-weight:900;font-size:40px;letter-spacing:.3px}
.hero-copy{position:absolute;left:75px;top:347px;width:440px;color:var(--white);font-size:16px;line-height:28.5px}

/* who */
.who-copy{position:absolute;left:0;width:1200px;text-align:center;font-size:16px;color:var(--text)}

/* why */
.why-band{position:absolute;left:0;top:1094px;width:1200px;height:558px;background:var(--grey)}
.why-list{position:absolute;left:75px;top:1254px;width:505px;list-style:none}
.why-list li{position:relative;padding-left:33px;font-size:16px;line-height:26px;margin-bottom:18px;color:var(--text)}
.why-list li svg{position:absolute;left:0;top:6px}

/* benefits */
.benefit{position:absolute;top:1810px;width:200px;text-align:center}
.benefit svg{display:block;margin:0 auto 16px}
.benefit p{font-size:16px;line-height:27px;color:var(--text);margin:0 auto}

/* software */
.soft-band{position:absolute;left:0;top:2068px;width:1200px;height:558px;background:var(--grey)}
.soft-copy{position:absolute;left:616px;top:2262px;width:505px;font-size:16px;line-height:34px;color:var(--text)}

/* contact */
.field{position:absolute;border:1.5px solid var(--line);border-radius:36px;background:var(--white);font-size:18px;color:var(--ink);padding-left:24px;display:flex;align-items:center}
.field.message{align-items:flex-start;padding-top:28px;border-radius:30px}
.submit{font-size:28px}
.guarantee{position:absolute;left:705px;top:2722px;width:420px;height:512px;background:var(--yellow);border-radius:28px;text-align:center}
.guarantee h3{margin-top:34px;font-weight:900;font-size:34px;color:var(--ink)}
.guarantee-badge{position:absolute;left:110px;top:92px;width:200px;height:166px;border-radius:20px;background:linear-gradient(180deg,#2a2f52 0%,var(--navy) 100%)}
.guarantee p{position:absolute;left:30px;right:30px;top:282px;font-size:17.5px;line-height:32.5px;color:var(--ink)}

/* footer */
.footer-bar{position:absolute;left:0;top:3325px;width:1200px;height:92px;background:var(--dark);border-bottom:1px solid #333}
.footer-bar .copy{position:absolute;left:75px;top:38px;color:var(--white);font-size:16px}
.socials{position:absolute;right:75px;top:32px;display:flex;gap:26px}
.socials span{width:26px;height:26px;border-radius:50%;background:var(--white)}
.disclaimer{position:absolute;left:0;top:3417px;width:1200px;height:221px;background:var(--darker);padding:44px 75px 0}
.disclaimer h4{color:var(--yellow);font-size:16px;font-weight:700;margin-bottom:6px}
.disclaimer p{color:#dddddd;font-size:13.6px;line-height:26px}
</style>
</head>
<body>

<!-- Hero -->
<section class="hero">
  <div class="hero-shade" role="img" aria-label="Smiling warehouse worker in hard hat and safety vest using a laptop between warehouse racks"></div>
  <div class="brand"><span class="brand-dot"></span>KEELHAVEN 3PL</div>
  <div class="hero-phone">
    <svg width="20" height="22" viewBox="0 0 20 22"><path d="M4 1 L8 1 L9 6 L6.5 8 C7.5 11 9.5 13.5 12.5 15 L14.5 12.5 L19 14 L19 18 C19 20 17 21 15 21 C8 20 1 13 1 5 C1 3 2 1 4 1Z" fill="var(--yellow)"/></svg>
    1-800-555-0142
  </div>
  <div class="menu-icon"><span></span><span></span><span></span></div>
  <h1>WELCOME TO KEELHAVEN 3PL</h1>
  <p class="hero-copy">Keelhaven 3PL is your one stop 3PL that will help you grow your business and allow you to be handsoff.<br>We offer high end services and meet our commitment, guaranteed.</p>
  <div class="btn" style="left:75px;top:483px;width:200px;height:59px">READ MORE</div>
</section>

<!-- Who we are -->
<h2 class="section-title" style="left:0;width:1200px;text-align:center;top:805px">WHO WE ARE</h2>
<p class="who-copy" style="top:872px">Keelhaven 3PL is your one stop 3PL that will help you grow your business and allow you to be handsoff.</p>
<p class="who-copy" style="top:906px">We offer high end services and meet our commitment, guaranteed.</p>
<div class="btn" style="left:500px;top:966px;width:199px;height:59px">READ MORE</div>

<!-- Why use a prep 3PL -->
<div class="why-band"></div>
<svg class="abs" style="left:600px;top:1086px" width="600" height="576" viewBox="0 0 600 576" role="img" aria-label="Two warehouse staff in safety vests working at a laptop beside stocked shelves">
  <defs><linearGradient id="whyPhoto" x1="0" y1="0" x2="1" y2="1"><stop offset="0" stop-color="#b89a78"/><stop offset=".5" stop-color="#8a7560"/><stop offset="1" stop-color="#4d4a44"/></linearGradient></defs>
  <path d="M20,0 C-25,200 70,450 290,576 L600,576 L600,0 Z" fill="url(#whyPhoto)"/>
  <path d="M20,0 C-25,200 70,450 290,576" fill="none" stroke="var(--yellow)" stroke-width="8"/>
</svg>
<h2 class="section-title" style="left:75px;top:1188px;font-size:33px">WHY USE A PREP 3PL?</h2>
<ul class="why-list">
  <li><svg width="16" height="16" viewBox="0 0 16 16"><circle cx="8" cy="8" r="8" fill="var(--yellow)"/><path d="M4.5 8.2 L7 10.5 L11.5 5.5" stroke="#fff" stroke-width="1.8" fill="none"/></svg>Work from anywhere in the world.</li>
  <li><svg width="16" height="16" viewBox="0 0 16 16"><circle cx="8" cy="8" r="8" fill="var(--yellow)"/><path d="M4.5 8.2 L7 10.5 L11.5 5.5" stroke="#fff" stroke-width="1.8" fill="none"/></svg>Don’t have to manage employees, health insurance plans, payroll, sick calls, etc.</li>
  <li><svg width="16" height="16" viewBox="0 0 16 16"><circle cx="8" cy="8" r="8" fill="var(--yellow)"/><path d="M4.5 8.2 L7 10.5 L11.5 5.5" stroke="#fff" stroke-width="1.8" fill="none"/></svg>Don’t get locked into a 3-5 year warehouse lease where you guarantee hundreds of thousands of dollars</li>
  <li><svg width="16" height="16" viewBox="0 0 16 16"><circle cx="8" cy="8" r="8" fill="var(--yellow)"/><path d="M4.5 8.2 L7 10.5 L11.5 5.5" stroke="#fff" stroke-width="1.8" fill="none"/></svg>Grow your business without commitment.</li>
</ul>
<div class="btn" style="left:74px;top:1509px;width:199px;height:59px">READ MORE</div>

<!-- Benefits -->
<h2 class="section-title" style="left:0;width:1200px;text-align:center;top:1730px">BENEFITS</h2>
<div class="benefit" style="left:71px">
  <svg width="82" height="82" viewBox="0 0 82 82"><circle cx="41" cy="41" r="38" fill="none" stroke="var(--yellow)" stroke-width="3"/><circle cx="41" cy="41" r="31" fill="none" stroke="var(--yellow)" stroke-width="2"/><path d="M41 18 V41 L56 50" fill="none" stroke="var(--yellow)" stroke-width="3" stroke-linecap="round"/></svg>
  <p style="width:180px">48 hour turn around guarantee – done in 48 hours or its free*</p>
</div>
<div class="benefit" style="left:285px">
  <svg width="82" height="82" viewBox="0 0 82 82"><rect x="8" y="6" width="66" height="44" rx="3" fill="none" stroke="var(--yellow)" stroke-width="3"/><line x1="8" y1="18" x2="74" y2="18" stroke="var(--yellow)" stroke-width="3"/><rect x="16" y="26" width="20" height="10" fill="none" stroke="var(--yellow)" stroke-width="2"/><path d="M34 80 V46 a5 5 0 0 1 10 0 V62 L56 64 V80" fill="none" stroke="var(--yellow)" stroke-width="3"/></svg>
  <p style="width:192px">No monthly subscription – only pay for what you use</p>
</div>
<div class="benefit" style="left:501px">
  <svg width="82" height="82" viewBox="0 0 82 82"><circle cx="41" cy="41" r="37" fill="none" stroke="var(--yellow)" stroke-width="3" stroke-dasharray="6 3"/><circle cx="41" cy="41" r="27" fill="none" stroke="var(--yellow)" stroke-width="2.5"/><path d="M18 58 L64 24" stroke="var(--yellow)" stroke-width="8"/></svg>
  <p style="width:110px">No receiving fees</p>
</div>
<div class="benefit" style="left:716px">
  <svg width="82" height="82" viewBox="0 0 82 82"><rect x="4" y="4" width="74" height="18" fill="none" stroke="var(--yellow)" stroke-width="3"/><circle cx="58" cy="48" r="12" fill="none" stroke="var(--yellow)" stroke-width="3"/><path d="M4 66 H26 L40 60 a4 4 0 0 1 4 6 L30 76 H4" fill="none" stroke="var(--yellow)" stroke-width="3"/></svg>
  <p style="width:180px">No pallet or outbound fees</p>
</div>
<div class="benefit" style="left:931px">
  <svg width="82" height="82" viewBox="0 0 82 82"><rect x="4" y="4" width="44" height="34" rx="4" fill="none" stroke="var(--yellow)" stroke-width="3"/><path d="M14 38 L10 50 L24 38" fill="none" stroke="var(--yellow)" stroke-width="3"/><rect x="26" y="36" width="52" height="40" fill="none" stroke="var(--yellow)" stroke-width="3"/><path d="M26 36 L52 58 L78 36" fill="none" stroke="var(--yellow)" stroke-width="3"/></svg>
  <p style="width:140px">Email and phone support</p>
</div>

<!-- Software -->
<div class="soft-band"></div>
<svg class="abs" style="left:0;top:2059px" width="600" height="576" viewBox="0 0 600 576" role="img" aria-label="Hands holding a tablet showing warehouse management dashboard charts in a warehouse aisle">
  <defs><linearGradient id="softPhoto" x1="0" y1="0" x2="1" y2="1"><stop offset="0" stop-color="#3c4350"/><stop offset=".55" stop-color="#5d6470"/><stop offset="1" stop-color="#a9a39b"/></linearGradient></defs>
  <path d="M0,0 L572,0 C612,150 520,450 282,576 L0,576 Z" fill="url(#softPhoto)"/>
  <path d="M572,0 C612,150 520,450 282,576" fill="none" stroke="var(--yellow)" stroke-width="8"/>
</svg>
<h2 class="section-title" style="left:616px;top:2198px">OUR SOFTWARE</h2>
<p class="soft-copy">Know what inventory is at our warehouse in real time.<br>Our software allows you to track your inventory and know how your shipment status in real time. Professional software designed specifically for our needs</p>
<div class="btn" style="left:616px;top:2429px;width:199px;height:59px">REQUEST DEMO</div>

<!-- Contact -->
<h2 class="section-title" style="left:75px;top:2714px">CONTACT FORM</h2>
<div class="field" style="left:75px;top:2789px;width:289px;height:70px">Name</div>
<div class="field" style="left:385px;top:2789px;width:290px;height:70px">Email Address</div>
<div class="field" style="left:75px;top:2876px;width:289px;height:71px">Phone No</div>
<div class="field" style="left:385px;top:2876px;width:290px;height:71px">Subject</div>
<div class="field message" style="left:75px;top:2962px;width:600px;height:187px">Message</div>
<div class="btn submit" style="left:75px;top:3163px;width:289px;height:71px">SUBMIT</div>

<div class="guarantee">
  <h3>OUR GUARANTEE</h3>
  <div class="guarantee-badge" role="img" aria-label="Guarantee shield badge with ribbon"></div>
  <p>All orders will be prepped and ready for shipment in 48 business hours (often 24 or less) and we guarantee it. We are confident in our services and if we do not fulfill our obligation, we offer a500 item (up to $700) credit on your next shipment.</p>
</div>

<!-- Footer -->
<footer>
  <div class="footer-bar">
    <div class="copy">Copyright © 2021. Company Name.&nbsp; All Right Reserved</div>
    <div class="socials"><span></span><span></span><span></span><span></span><span></span></div>
  </div>
  <div class="disclaimer">
    <h4>Disclaimer</h4>
    <p>*Our guarantee is 48 hours from the time an outbound shipment is created in our system. Weekends and holidays excluded. Orders created on a Friday after hours, Saturday or Sunday will be counted from the open of business on Monday morning. We offer a credit of up to 500 units on your next shipment. These credits are for standard prep items only, no bundles, bubble wrapped or multipack units. Outbound shipments will be prepped and ready to ship. We are unable to control shipping companies and freight carriers. Orders after daily pickups are completed will be ready for next day pickup.</p>
  </div>
</footer>

</body>
</html>
```